Marcus Delwyn-Hart Finance

Need a personal website advertising Equipment Finance,Business Finance,Commercial Finance, Construction Finance, Bridging Finance. Similar websites are www.qorvimark.com.au / www.talsbrio.com.au / www.zpk7.com.au /wwwlemberwick.com.au

Target Market(s)

Business People

Industry/Entity Type

Business

Number of Pages Required

3 page

Font styles to use
Serif
Sans Serif

Requirements
Must have
• All i want is a simple corporate looking website advertising Equipment Finance, Commercial Finance, Construction Finance, Business Finance, Bridging Finance,

```html
<!DOCTYPE html>
<html lang="en">
<head>
<meta charset="utf-8">
<title>Halvern Finance</title>
<link href="https://fonts.googleapis.com/css2?family=Open+Sans:wght@400;600;700;800&display=swap" rel="stylesheet">
<style>
:root{
  --blue:#1f5fb8;
  --blue-dark:#174a93;
  --ink:#1d1d1d;
  --text:#555;
  --muted:#8a8a8a;
  --line:#dcdcdc;
  --footer:#121212;
  --white:#fff;
}
*{box-sizing:border-box;margin:0;padding:0}
html,body{width:885px;height:1200px;overflow:hidden}
body{font-family:"Open Sans",Arial,sans-serif;color:var(--ink);background:var(--white);position:relative}
a{text-decoration:none;color:inherit}

/* header */
.site-header{position:absolute;top:0;left:0;width:885px;height:41px;background:var(--white);display:flex;align-items:center;padding:0 40px;z-index:2}
.brand{display:flex;align-items:center;gap:8px;font-size:20px;font-weight:700;color:var(--blue);white-space:nowrap}
.brand-mark{width:22px;height:22px;background:var(--blue)}
.main-nav{margin-left:auto;display:flex;gap:22px;font-size:9px;font-weight:700;color:#333;letter-spacing:.3px}
.main-nav a.active{color:var(--blue)}
.header-call{margin-left:26px;display:flex;align-items:center;gap:6px;font-size:9px;font-weight:700;line-height:1.2;white-space:nowrap}
.header-call .label{color:var(--blue)}

/* hero */
.hero{position:absolute;top:41px;left:0;width:885px;height:404px;background:linear-gradient(160deg,#c9d9ec 0%,#9fb3c9 35%,#7d8ea2 60%,#b9c6d4 100%)}
.hero-caption{position:absolute;right:30px;top:168px;width:318px;height:120px;background:rgba(20,20,20,.72);padding:14px 20px;color:var(--white)}
.hero-caption h2{font-size:22px;font-weight:700;margin-bottom:6px;white-space:nowrap}
.hero-caption p{font-size:9px;line-height:1.5;color:#ddd;width:270px}
.btn{display:inline-block;background:var(--blue);color:var(--white);font-size:8px;font-weight:700;padding:7px 14px;letter-spacing:.4px;white-space:nowrap}
.hero-caption .btn{position:absolute;right:20px;bottom:12px}

/* welcome */
.welcome{position:absolute;top:445px;left:0;width:885px;height:284px}
.welcome-copy{position:absolute;left:74px;top:48px;width:430px}
.welcome-copy h1{font-size:18px;font-weight:800;letter-spacing:.3px;white-space:nowrap}
.welcome-copy h1 span{color:var(--blue)}
.welcome-copy .rule{width:40px;height:3px;background:var(--blue);margin:8px 0 14px}
.welcome-copy p{font-size:9px;line-height:1.65;color:var(--text);margin-bottom:16px}
.inquiry{position:absolute;left:603px;top:22px;width:210px;height:236px;background:#f1f1f1;border:1px solid var(--line);padding:10px 14px}
.inquiry h3{font-size:14px;font-weight:800;text-align:center;letter-spacing:.3px}
.inquiry .rule{width:40px;height:2px;background:var(--blue);margin:6px auto 10px}
.field{background:var(--white);border:1px solid var(--line);height:20px;font-size:7px;color:var(--muted);padding:5px 6px;margin-bottom:6px}
.field.message{height:52px}
.inquiry .btn{display:block;text-align:center;margin-top:4px}

/* services */
.services{position:absolute;top:729px;left:0;width:885px;height:238px;background:linear-gradient(135deg,var(--blue-dark),#2e72cf 50%,var(--blue-dark))}
.services h2{text-align:center;color:var(--white);font-size:18px;font-weight:800;margin-top:30px}
.services .rule{width:40px;height:2px;background:var(--white);margin:8px auto 0}
.service-list{display:flex;justify-content:center;gap:6px;margin-top:24px}
.service{width:150px;text-align:center}
.service-icon{width:72px;height:72px;margin:0 auto;background:var(--white);border:2px solid #dfe8f5;display:flex;align-items:center;justify-content:center}
.service-name{display:block;margin-top:10px;color:var(--white);font-size:10px;font-weight:600;white-space:nowrap}

/* footer */
.site-footer{position:absolute;top:967px;left:0;width:885px;height:215px;background:var(--footer);color:#ccc}
.footer-col{position:absolute;top:30px}
.footer-col h4{font-size:10px;font-weight:800;color:var(--white);letter-spacing:.3px;white-space:nowrap}
.footer-col h4 span{color:var(--blue)}
.footer-col .rule{width:30px;height:2px;background:var(--blue);margin:6px 0 10px}
.links li{list-style:none;font-size:8px;line-height:2;color:#ccc}
.links li::before{content:"›";color:var(--blue);margin-right:5px}
.contact-row{display:flex;gap:6px;font-size:8px;line-height:1.5;margin-bottom:8px;color:#ccc}
.contact-row strong{color:var(--white)}
.map{width:120px;height:75px;background:linear-gradient(135deg,#e7e4dc,#d6d3c8);border:3px solid var(--white)}
.footer-brand{position:absolute;right:45px;top:40px;text-align:right}
.footer-brand .name{display:flex;align-items:center;gap:6px;justify-content:flex-end;font-size:13px;font-weight:700;color:var(--white);white-space:nowrap}
.footer-brand .name i{width:14px;height:14px;background:var(--white)}
.social{display:flex;gap:4px;justify-content:flex-end;margin-top:40px}
.social span{width:14px;height:14px;background:var(--blue)}
.copyright{position:absolute;bottom:0;left:0;width:885px;height:18px;background:var(--blue);color:var(--white);font-size:7px;text-align:center;line-height:18px}
</style>
</head>
<body>

<header class="site-header">
  <a class="brand" href="#"><span class="brand-mark"></span>Halvern Finance</a>
  <nav class="main-nav">
    <a class="active" href="#">HOME</a><a href="#">ABOUT US</a><a href="#">SERVICES</a><a href="#">CONTACT US</a>
  </nav>
  <div class="header-call">
    <svg width="16" height="16" viewBox="0 0 24 24"><circle cx="12" cy="12" r="12" fill="#1f5fb8"/><path d="M8 6l2 0 1 3-1.5 1a7 7 0 0 0 4 4l1-1.5 3 1v2a2 2 0 0 1-2 2A10 10 0 0 1 6 8a2 2 0 0 1 2-2z" fill="#fff"/></svg>
    <div><span class="label">CALL US</span><br>(02) 5550 1847</div>
  </div>
</header>

<section class="hero" role="img" aria-label="Businessman in a suit looking out over city office towers">
  <div class="hero-caption">
    <h2>Construction Finance</h2>
    <p>Flexible funding for builders and developers across every stage of the project.</p>
    <a class="btn" href="#">CALL US TODAY</a>
  </div>
</section>

<section class="welcome">
  <div class="welcome-copy">
    <h1>WELCOME TO <span>HALVERN FINANCE</span></h1>
    <div class="rule"></div>
    <p>We help business owners secure the funding they need to grow. From new equipment and vehicles to commercial property and construction projects, our team compares lenders to find terms that suit your cash flow. Talk to us today for clear advice, fast approvals and a simple process from first call to settlement.</p>
    <a class="btn" href="#">READ MORE</a>
  </div>
  <form class="inquiry">
    <h3>QUICK INQUIRY</h3>
    <div class="rule"></div>
    <div class="field">Name</div>
    <div class="field">Email</div>
    <div class="field">Phone</div>
    <div class="field message">Message</div>
    <a class="btn" href="#">SUBMIT</a>
  </form>
</section>

<section class="services">
  <h2>OUR SERVICES</h2>
  <div class="rule"></div>
  <div class="service-list">
    <div class="service">
      <div class="service-icon"><svg width="40" height="36" viewBox="0 0 34 30"><rect x="2" y="14" width="18" height="8" fill="#111"/><rect x="8" y="8" width="8" height="7" fill="#111"/><path d="M18 14L26 4l5 8" stroke="#111" stroke-width="3" fill="none"/><rect x="1" y="23" width="20" height="5" rx="2.5" fill="#111"/></svg></div>
      <span class="service-name">Equipment Finance</span>
    </div>
    <div class="service">
      <div class="service-icon"><svg width="36" height="36" viewBox="0 0 30 30"><rect x="3" y="10" width="24" height="16" rx="2" fill="#111"/><rect x="11" y="5" width="8" height="6" fill="none" stroke="#111" stroke-width="2"/><rect x="3" y="16" width="24" height="2" fill="#fff"/></svg></div>
      <span class="service-name">Business Finance</span>
    </div>
    <div class="service">
      <div class="service-icon"><svg width="38" height="36" viewBox="0 0 32 30"><rect x="2" y="8" width="10" height="20" fill="#111"/><rect x="13" y="2" width="8" height="26" fill="#111"/><rect x="22" y="12" width="8" height="16" fill="#111"/></svg></div>
      <span class="service-name">Commercial Finance</span>
    </div>
    <div class="service">
      <div class="service-icon"><svg width="38" height="36" viewBox="0 0 32 30"><rect x="8" y="4" width="3" height="24" fill="#111"/><rect x="4" y="4" width="26" height="3" fill="#111"/><line x1="26" y1="7" x2="26" y2="15" stroke="#111" stroke-width="1.5"/><rect x="23" y="15" width="6" height="4" fill="#111"/><rect x="4" y="26" width="12" height="3" fill="#111"/></svg></div>
      <span class="service-name">Construction Finance</span>
    </div>
    <div class="service">
      <div class="service-icon"><svg width="40" height="36" viewBox="0 0 34 30"><rect x="1" y="18" width="32" height="3" fill="#111"/><rect x="8" y="6" width="3" height="20" fill="#111"/><rect x="23" y="6" width="3" height="20" fill="#111"/><path d="M1 18Q9.5 6 9.5 6T24.5 6 33 18" stroke="#111" stroke-width="1.5" fill="none"/></svg></div>
      <span class="service-name">Bridging Finance</span>
    </div>
  </div>
</section>

<footer class="site-footer">
  <div class="footer-col" style="left:74px">
    <h4>QUICK <span>LINKS</span></h4>
    <div class="rule"></div>
    <ul class="links"><li>HOME</li><li>ABOUT US</li><li>SERVICES</li><li>CONTACT US</li></ul>
  </div>
  <div class="footer-col" style="left:240px;width:180px">
    <h4>CONTACT <span>DETAILS</span></h4>
    <div class="rule"></div>
    <div class="contact-row">
      <svg width="9" height="11" viewBox="0 0 10 14"><path d="M5 0a5 5 0 0 1 5 5c0 4-5 9-5 9S0 9 0 5a5 5 0 0 1 5-5z" fill="#1f5fb8"/><circle cx="5" cy="5" r="2" fill="#121212"/></svg>
      <div><strong>Halvern Finance</strong><br>Level 4, 210 Harbour Street,<br>Sydney NSW 2000</div>
    </div>
    <div class="contact-row">
      <svg width="9" height="9" viewBox="0 0 24 24"><path d="M5 2l4 0 2 5-3 2a11 11 0 0 0 7 7l2-3 5 2v4a2 2 0 0 1-2 2A19 19 0 0 1 3 4a2 2 0 0 1 2-2z" fill="#1f5fb8"/></svg>
      <div>(02) 5550 1847</div>
    </div>
    <div class="contact-row">
      <svg width="10" height="8" viewBox="0 0 20 14"><rect width="20" height="14" fill="#1f5fb8"/><path d="M0 0l10 8 10-8" stroke="#121212" stroke-width="1.5" fill="none"/></svg>
      <div>info@halvernfinance.com.au</div>
    </div>
  </div>
  <div class="footer-col" style="left:460px">
    <h4>LOCATION <span>MAP</span></h4>
    <div class="rule"></div>
    <div class="map" role="img" aria-label="Street map showing the office location"></div>
  </div>
  <div class="footer-brand">
    <div class="name"><i></i>Halvern Finance</div>
    <div class="social"><span></span><span></span><span></span><span></span></div>
  </div>
</footer>
<div class="copyright">Copyright © 2019 Halvern Finance. All Rights Reserved.</div>

</body>
</html>
```